EPIC, awesome, creative business card needed - get involved!

I'm launching a boutique, exclusive Property Management real estate agency in Sydney early next year.
The name of the agency will be called "Quartz Hill Lane" - it's a play on "chase the silver pebble trail" to wealth. The Quartz Hill Lane signifies wealth through property investment.
My business will offer management of investment properties (ie Property Management).
The difference with Quartz Hill Lane and other agencies is the business will be run by one of Australia's leading property investment experts, and also one of Australia's leading property managers.
It will be exclusively for high net worth properties and individuals, so the business card needs to be extremely sharp, slick and relatively simple.
The information I want on the card is as follows
Nolan Pryce - Director
M: 0412 967 154
P: 9735 6021
E: nolan@quartzhilllane.net.au
W: quartzhilllane.net.au
I'm happy with the red from the logo, black - no yellows or funky colors. I want this to be a super corporate and slick business card to match the high end nature of the business.
Good luck everyone, and please ask questions for clarification.

```html
<!DOCTYPE html>
<html lang="en">
<head>
<meta charset="utf-8">
<title>Quartz Hill Lane – Business Card</title>
<link href="https://fonts.googleapis.com/css2?family=Open+Sans:wght@400;600;700&display=swap" rel="stylesheet">
<style>
  :root {
    --brand-red: #c20a1e;
    --brand-red-deep: #a8081a;
    --ink: #2b2b2b;
    --paper: #f7f7f7;
    --stage: #2a2a2a;
    --white: #ffffff;
  }
  * { margin: 0; padding: 0; box-sizing: border-box; }
  html, body {
    width: 1200px; height: 900px; overflow: hidden;
    background: var(--stage);
    font-family: "Open Sans", Arial, sans-serif;
  }
  .canvas {
    width: 1200px; height: 900px;
    display: flex; flex-direction: column;
    align-items: center; justify-content: center; gap: 40px;
  }
  .card {
    width: 680px; height: 390px;
    position: relative;
    box-shadow: 0 10px 30px rgba(0,0,0,.45);
  }
  .card--back { background: var(--brand-red); }
  .card--front { background: var(--paper); color: var(--ink); }

  .brand {
    display: flex; align-items: center; gap: 18px;
  }
  .brand__square { width: 110px; height: 110px; flex: none; }
  .brand__name {
    font-weight: 700; font-size: 34px; line-height: 1.02;
    text-transform: uppercase; letter-spacing: .02em;
  }
  .card--back .brand {
    position: absolute; left: 50%; top: 50%;
    transform: translate(-50%, -50%);
  }
  .card--back .brand__square { background: var(--brand-red-deep); }
  .card--back .brand__name { color: var(--white); }

  .card--front .brand {
    position: absolute; right: 56px; top: 52px;
  }
  .card--front .brand__square { background: var(--brand-red); }
  .card--front .brand__name { color: var(--brand-red); }

  .website {
    position: absolute; right: 56px; top: 196px;
    font-size: 15px; letter-spacing: .02em;
  }

  .person { position: absolute; left: 56px; top: 150px; }
  .person__name { color: var(--brand-red); font-weight: 600; font-size: 20px; }
  .person__role { font-size: 14px; margin-top: 2px; }

  .contact { list-style: none; margin-top: 18px; font-size: 15px; line-height: 1.5; }
  .contact__label { color: var(--brand-red); display: inline-block; width: 22px; }

  .address { margin-top: 30px; font-size: 16px; line-height: 1.4; }
</style>
</head>
<body>
<main class="canvas">
  <section class="card card--back" aria-label="Card back">
    <div class="brand">
      <span class="brand__square"></span>
      <span class="brand__name">Quartz<br>Hill<br>Lane</span>
    </div>
  </section>

  <section class="card card--front" aria-label="Card front">
    <div class="brand">
      <span class="brand__square"></span>
      <span class="brand__name">Quartz<br>Hill<br>Lane</span>
    </div>
    <p class="website">www.quartzhilllane.net.au</p>

    <div class="person">
      <p class="person__name">Nolan Pryce</p>
      <p class="person__role">Director</p>
      <ul class="contact">
        <li><span class="contact__label">M</span>0412 967 154</li>
        <li><span class="contact__label">P</span>9735 6021</li>
        <li><span class="contact__label">E</span>nolan@quartzhilllane.net.au</li>
      </ul>
      <p class="address">18th Terrace, Harbourview<br>Sydney, NSW, Australia</p>
    </div>
  </section>
</main>
</body>
</html>
```